KMT Law Firm Business Card

We need a business card design for our law firm. We recently had a name change and so we have a new logo. We are a small plaintiff's law firm in Oklahoma but do work all over the USA We have a new logo (see attached the artwork in both black & brown – could also reverse the logo so that it’s white) We'd like an upscale western design. One side needs the logo and this slogan : "Clients-Conviction-Courage Always aim for more"
and on the other side needs to be a template so we can fill in the attorney's name --include this info:
Whitcombe Whitcombe Delacroix
-------Attorneys------------
(name of attorney) ie: Howard T. Whitcombe
(title) ie: Attorney/Managing Partner
5812 S. Garnet Tulsa, OK 74139
918-555-0143
Fax 918-555-0178
(name)@kmtlegal.example www.kmtlegal.example ie: hank@kmtlegal.example
also needs a small Facebook & twitter logo -
and 3 of the attorneys need the circle logo attached that says "Grand Verdict Litigators Circle" - so we need to be able to remove that for some of the designs –

Industry/Entity Type

Law Firm

```html
<!DOCTYPE html>
<html lang="en">
<head>
<meta charset="utf-8">
<title>Whitcombe Whitcombe Delacroix – Business Card</title>
<link href="https://fonts.googleapis.com/css2?family=Open+Sans:wght@400;600;700&display=swap" rel="stylesheet">
<style>
  :root {
    --stage: #c9c9c9;
    --card-white: #ffffff;
    --card-black: #0e0e0f;
    --card-charcoal: #2a2b2d;
    --ink-dark: #1a1a1a;
    --ink-silver: #a9a9ab;
    --ink-light: #f2f2f2;
    --ink-muted: #c8c8c8;
    --rule: #8a8a8a;
  }
  * { box-sizing: border-box; margin: 0; padding: 0; }
  html, body { width: 1200px; height: 900px; overflow: hidden; }
  body {
    background: var(--stage);
    font-family: "Open Sans", sans-serif;
    display: flex;
    align-items: center;
    justify-content: center;
    gap: 44px;
  }
  .card {
    position: relative;
    width: 540px;
    height: 320px;
    border-radius: 24px;
    overflow: hidden;
    box-shadow: 0 14px 30px rgba(0,0,0,0.28);
  }

  /* Front */
  .card-front { background: var(--card-black); }
  .front-top {
    height: 150px;
    background: var(--card-white);
    display: flex;
    align-items: center;
    justify-content: center;
  }
  .silver-band {
    height: 10px;
    background: linear-gradient(90deg, #6e6e6e 0%, #e9e9e9 35%, #9c9c9c 60%, #f4f4f4 85%, #7a7a7a 100%);
  }
  .front-bottom {
    height: 160px;
    background: radial-gradient(ellipse at 50% 0%, var(--card-charcoal) 0%, var(--card-black) 75%);
    display: flex;
    align-items: center;
    padding: 0 20px 0 22px;
  }
  .identity { width: 206px; text-align: right; padding-right: 14px; white-space: nowrap; }
  .attorney-name { color: var(--ink-muted); font-size: 17px; font-weight: 600; line-height: 1.2; }
  .attorney-title { color: var(--ink-muted); font-size: 11.5px; margin-top: 2px; }
  .divider { width: 1px; height: 112px; background: var(--rule); }
  .contact-list { list-style: none; padding-left: 14px; white-space: nowrap; }
  .contact-list li {
    display: flex; align-items: center; gap: 8px;
    color: var(--ink-light); font-size: 14px; line-height: 21px;
  }
  .contact-list svg { width: 13px; height: 13px; flex: none; fill: var(--ink-muted); }

  /* Firm name mark */
  .firm-mark { display: flex; align-items: center; gap: 10px; }
  .firm-mark .dot { width: 14px; height: 14px; border-radius: 50%; }
  .firm-name {
    font-size: 16px; font-weight: 700; letter-spacing: 1.5px; text-transform: uppercase;
    white-space: nowrap;
  }
  .card-front .firm-name { color: var(--ink-dark); }
  .card-front .dot { background: var(--ink-dark); }

  /* Back */
  .card-back {
    background: radial-gradient(ellipse at 50% 40%, #2e2f31 0%, #141415 55%, var(--card-black) 100%);
  }
  .back-logo {
    position: absolute; left: 0; right: 0; top: 115px;
    display: flex; justify-content: center;
  }
  .card-back .firm-name { color: var(--ink-silver); }
  .card-back .dot { background: var(--ink-silver); }
  .slogan {
    position: absolute; left: 0; right: 0; bottom: 40px;
    text-align: center;
    color: var(--ink-light);
    font-size: 14px; font-weight: 600;
    font-variant: small-caps;
    letter-spacing: 2.6px;
    white-space: nowrap;
  }
</style>
</head>
<body>

<section class="card card-front" aria-label="Business card front">
  <div class="front-top">
    <div class="firm-mark">
      <span class="dot"></span>
      <span class="firm-name">Whitcombe Whitcombe Delacroix</span>
    </div>
  </div>
  <div class="silver-band"></div>
  <div class="front-bottom">
    <div class="identity">
      <p class="attorney-name">Howard T. Whitcombe</p>
      <p class="attorney-title">Attorney/Managing Partner</p>
    </div>
    <div class="divider"></div>
    <ul class="contact-list">
      <li><svg viewBox="0 0 24 24"><path d="M12 2a7 7 0 0 0-7 7c0 5 7 13 7 13s7-8 7-13a7 7 0 0 0-7-7zm0 9.5A2.5 2.5 0 1 1 12 6.5a2.5 2.5 0 0 1 0 5z"/></svg>5812 S. Garnet Tulsa, OK 74139</li>
      <li><svg viewBox="0 0 24 24"><path d="M6.6 10.8a15 15 0 0 0 6.6 6.6l2.2-2.2a1 1 0 0 1 1-.25 11.4 11.4 0 0 0 3.6.57 1 1 0 0 1 1 1V20a1 1 0 0 1-1 1A17 17 0 0 1 3 4a1 1 0 0 1 1-1h3.5a1 1 0 0 1 1 1c0 1.250.2 2.45.57 3.57a1 1 0 0 1-.25 1z"/></svg>918-555-0143</li>
      <li><svg viewBox="0 0 24 24"><path d="M7 3h8l2 2v4H7zM4 10h16a2 2 0 0 1 2 2v6h-4v3H6v-3H2v-6a2 2 0 0 1 2-2zm4 7v2h8v-2z"/></svg>918-555-0178</li>
      <li><svg viewBox="0 0 24 24"><path d="M3 5h18a1 1 0 0 1 1 1v12a1 1 0 0 1-1 1H3a1 1 0 0 1-1-1V6a1 1 0 0 1 1-1zm9 7.5L20 7H4z"/></svg>hank@kmtlegal.example</li>
      <li><svg viewBox="0 0 24 24"><path d="M12 2a10 10 0 1 0 0 20 10 10 0 0 0 0-20zm6.9 6h-3a15 15 0 0 0-1.300-3.9A8 8 0 0 1 18.9 8zM12 4c.8 1.1 1.5 2.5 1.9 4h-3.8c.4-1.5 1.1-2.9 1.900-4zM4.3 14a8 8 0 0 1 0-4h3.4a16 16 0 0 0 0 4zm.8 2h3a15 15 0 0 0 1.3 3.9A8 8 0 0 1 5.1 16zm3-8h-3a8 8 0 0 1 4.3-3.9A15 15 0 0 0 8.1 8zM12 20c-.8-1.1-1.5-2.5-1.9-4h3.8c-.4 1.5-1.1 2.9-1.9 4zm2.3-6H9.7a14 14 0 0 1 0-4h4.6a14 14 0 0 1 0 4zm.3 5.9a15 15 0 0 0 1.3-3.9h3a8 8 0 0 1-4.3 3.9zm1.7-5.9a16 16 0 0 0 0-4h3.4a8 8 0 0 1 0 4z"/></svg>www.kmtlegal.example</li>
    </ul>
  </div>
</section>

<section class="card card-back" aria-label="Business card back">
  <div class="back-logo">
    <div class="firm-mark">
      <span class="dot"></span>
      <span class="firm-name">Whitcombe Whitcombe Delacroix</span>
    </div>
  </div>
  <p class="slogan">Clients-Conviction-Courage Always aim for more</p>
</section>

</body>
</html>
```